Bright Tooth Dentistry Business Card

We need business cards for our dental office.
We are looking for a clean, elegant design

We provide dental services to children.
Our card needs to be appealing to referring dentists, parents and our team

Target Market(s)

referring dentists, parents and our team

Industry/Entity Type

Dental Clinic

Contact Information for Business Card

4816 Juniper Lane, Suite 100
Fernwood Heights, OH 15237

412-837-2961 Voice
412-837-2962 fax
info@brighttoothdentalpa.com email
www.brighttoothdentalpa.com web

Font styles to use
Sans Serif

Requirements
Must have
• White background - clean, crisp, elegant, simple
• rounded corners
• different color palate - once we come up with design, we will replace the blue with orange, green,
Nice to have
• Follow our logo typeface and colors
• then we can replace color

```html
<!DOCTYPE html>
<html lang="en">
<head>
<meta charset="utf-8">
<title>Bright Tooth Dentistry Business Card</title>
<link href="https://fonts.googleapis.com/css2?family=Quicksand:wght@500;700&family=Open+Sans:wght@400&display=swap" rel="stylesheet">
<style>
  :root {
    --brand: #00adee;
    --ink: #3a3a3a;
    --muted: #6b6b6b;
    --card: #ffffff;
    --stage: #5f5f5f;
  }
  * { margin: 0; padding: 0; box-sizing: border-box; }
  html, body { width: 1200px; height: 1200px; overflow: hidden; }
  body { background: var(--stage); position: relative; font-family: "Open Sans", sans-serif; }

  .card {
    position: absolute;
    left: 240px;
    width: 720px;
    height: 420px;
    border-radius: 26px;
    overflow: hidden;
  }
  .card--front { top: 142px; background: var(--card); }
  .card--back { top: 638px; background: var(--brand); }

  .brand {
    position: absolute;
    display: flex;
    align-items: center;
    gap: 10px;
    font-family: "Quicksand", sans-serif;
    font-weight: 700;
    white-space: nowrap;
  }
  .brand__dot { border-radius: 50%; flex: none; }
  .card--front .brand { left: 31px; top: 132px; font-size: 33px; color: var(--brand); }
  .card--front .brand__dot { width: 16px; height: 16px; background: var(--brand); }
  .card--back .brand { left: 0; right: 0; top: 232px; justify-content: center; font-size: 46px; color: #fff; gap: 14px; }
  .card--back .brand__dot { width: 22px; height: 22px; background: #fff; }

  .person__name {
    position: absolute;
    right: 59px;
    top: 190px;
    font-family: "Quicksand", sans-serif;
    font-weight: 700;
    font-size: 20px;
    color: var(--brand);
  }
  .divider { position: absolute; top: 231px; height: 1.5px; background: var(--brand); }
  .divider--left { left: 0; width: 540px; }
  .divider--right { left: 626px; right: 0; }
  .person__role {
    position: absolute;
    left: 552px;
    top: 219px;
    font-family: "Quicksand", sans-serif;
    font-weight: 500;
    font-size: 18px;
    color: var(--muted);
  }

  .contacts { position: absolute; left: 36px; top: 286px; list-style: none; }
  .contacts li {
    display: flex;
    align-items: center;
    gap: 9px;
    height: 27.3px;
    font-size: 15px;
    color: var(--ink);
  }
  .contacts svg { width: 12px; height: 12px; fill: var(--brand); flex: none; }
  .contacts .accent { color: var(--brand); }

  .address {
    position: absolute;
    right: 59px;
    top: 348px;
    text-align: right;
    font-size: 15px;
    line-height: 20px;
    color: var(--ink);
    font-style: normal;
  }
</style>
</head>
<body>

<section class="card card--front">
  <div class="brand"><span class="brand__dot"></span>Bright Tooth Dentistry</div>

  <div class="person__name">Lena Farrow</div>
  <div class="divider divider--left"></div>
  <div class="person__role">Doctor</div>
  <div class="divider divider--right"></div>

  <ul class="contacts">
    <li>
      <svg viewBox="0 0 24 24"><path d="M6.6 10.8c1.4 2.8 3.8 5.1 6.6 6.6l2.2-2.2c.3-.3.7-.4 1-.2 1.1.4 2.3.6 3.6.6.6 0 1 .4 1 1V20c0 .6-.4 1-1 1C10.6 21 3 13.4 3 4c0-.6.4-1 1-1h3.5c.6 0 1 .4 1 1 0 1.2.2 2.4.6 3.6.1.3 0 .7-.2 1z"/></svg>
      412-837-2961
    </li>
    <li>
      <svg viewBox="0 0 24 24"><path d="M6 2h12v6H6zM3 9h18a1 1 0 0 1 1 1v7h-4v5H6v-5H2v-7a1 1 0 0 1 1-1zm5 7v4h8v-4z"/></svg>
      412-837-2962
    </li>
    <li>
      <svg viewBox="0 0 24 24"><path d="M2 4h20v16H2zm2 2v.5l8 5.5 8-5.5V6zm0 3v9h16V9l-8 5.5z"/></svg>
      info@brighttoothdentalpa.com
    </li>
    <li>
      <svg viewBox="0 0 24 24"><path d="M12 2a10 10 0 1 0 0 20 10 10 0 0 0 0-20zm-1 17.9A8 8 0 0 1 4.2 10.2L9 15v1a2 2 0 0 0 2 2zm6.9-2.5A2 2 0 0 0 16 16h-1v-3a1 1 0 0 0-1-1H8v-2h2a1 1 0 0 0 1-1V7h2a2 2 0 0 0 2-2v-.4a8 8 0 0 1 2.9 12.8z"/></svg>
      <span>www.<span class="accent">brighttoothdentalpa</span>.com</span>
    </li>
  </ul>

  <address class="address">
    4816 Juniper Lane, Suite 100<br>
    Fernwood Heights, OH 15237
  </address>
</section>

<section class="card card--back">
  <div class="brand"><span class="brand__dot"></span>Bright Tooth Dentistry</div>
</section>

</body>
</html>
```